Create a promo image to demo to a restaurant the increase in $ they can achieve by using Vesper

Create a promotional image to demonstrate to a restaurant the increase in revenue they can achieve by using Vesper.

We have constructed the attached example of what we are looking for, open to alternatives however the main message is you will make more money from a Vesper event than from your own restaurant for the same guests

We would like the restaurant image to look like the restaurant environment (show other tables in the background) and the same for the Customer dining room (plush private secure)

Please Vesper branding where it fits best

Target Market(s)

Restaurants to signup

Industry/Entity Type

Restaurants and Catering

Requirements
Must have
• Simplicity and obviousness

```html
<!DOCTYPE html>
<html lang="en">
<head>
<meta charset="utf-8">
<title>Vesper – More Income Beyond Your Four Walls</title>
<link href="https://fonts.googleapis.com/css2?family=Montserrat:wght@500;600;700;800&family=Pirata+One&family=Oswald:wght@400;500&display=swap" rel="stylesheet">
<style>
  :root {
    --paper: #ffffff;
    --plum: #8b2460;
    --plum-deep: #4b1a40;
    --plum-tag: #5c1f4c;
    --rule: rgba(255,255,255,0.75);
    --green: #6a9a3f;
    --teal: #006b67;
    --orange: #f6a623;
    --gold: #f7aa26;
    --ink: #000000;
    --white: #ffffff;
  }
  * { box-sizing: border-box; margin: 0; padding: 0; }
  html, body { width: 810px; height: 1200px; overflow: hidden; background: var(--paper); }
  body { position: relative; font-family: "Montserrat", sans-serif; color: var(--white); }

  .poster {
    position: absolute; left: 54px; top: 54px; width: 702px; height: 1092px;
    background: radial-gradient(ellipse at 50% 40%, #962a68 0%, var(--plum) 55%, #7a1f56 100%);
    overflow: hidden;
  }
  .abs { position: absolute; }

  .headline-band {
    left: 0; top: 19px; width: 702px; height: 63px; background: var(--plum-deep);
    text-align: center;
  }
  .headline-main { font-weight: 700; font-size: 28px; line-height: 1; margin-top: 9px; letter-spacing: 0.5px; }
  .headline-sub { font-weight: 700; font-size: 18.5px; line-height: 1; margin-top: 4px; letter-spacing: 0.3px; }

  .taglines { left: 0; top: 94px; width: 702px; text-align: center; font-weight: 700; font-size: 12.4px; line-height: 20.5px; letter-spacing: 0.3px; }

  .brand { left: 27px; top: 150px; width: 120px; height: 60px; display: flex; align-items: center; gap: 7px; }
  .brand-dot { width: 14px; height: 14px; border-radius: 50%; background: var(--plum-deep); }
  .brand-name { font-weight: 800; font-size: 24px; color: var(--plum-deep); }

  .feature-title {
    left: 150px; top: 154px; width: 400px; height: 66px; text-align: center;
    font-family: "Pirata One", serif; font-weight: 400; font-size: 62px; line-height: 66px;
    white-space: nowrap;
    text-shadow: 3px 4px 6px rgba(40,5,30,0.6);
  }

  .uplift { left: 566px; top: 140px; width: 108px; height: 72px; background: var(--plum-deep); }
  .uplift-frame {
    position: absolute; left: 7px; top: 7px; width: 94px; height: 58px; border: 1.5px solid var(--white);
    font-family: "Oswald", sans-serif; font-weight: 500; font-size: 40px; line-height: 56px; text-align: center;
  }
  .uplift-frame sup { font-size: 19px; vertical-align: top; line-height: 34px; }

  .covers-band {
    left: 216px; top: 226px; width: 269px; height: 39px; background: var(--plum-deep);
    text-align: center; font-weight: 700; font-size: 29px; line-height: 40px; letter-spacing: 0.5px;
  }

  .divider-h { left: 0; top: 264px; width: 702px; height: 1.5px; background: var(--plum-deep); }
  .divider-v { left: 350px; top: 265px; width: 1.5px; height: 752px; background: var(--plum-deep); }

  .column-head {
    top: 280px; width: 296px; height: 39px; background: var(--plum-deep);
    text-align: center; font-weight: 700; font-size: 20.5px; line-height: 40px; letter-spacing: 0.3px;
  }
  .column-head span { color: var(--gold); }

  .course { width: 296px; }
  .course-head { height: 36px; border-bottom: 1.5px solid var(--rule); display: flex; align-items: center; gap: 9px; }
  .course-name { font-family: "Pirata One", serif; font-size: 28px; line-height: 1; }
  .price-tag { background: var(--plum-tag); font-weight: 700; font-size: 12.5px; padding: 3px 8px; letter-spacing: 0.4px; }
  .mode-labels { display: flex; justify-content: space-between; font-weight: 700; font-size: 12.4px; letter-spacing: 0.5px; height: 36px; padding-top: 9px; }
  .course-boxes { display: flex; justify-content: space-between; margin-top: 14px; }
  .course-boxes.tight { margin-top: 0; }

  .tally { width: 139px; height: 103px; border: 1.5px solid var(--rule); padding: 13px 0 0 13px; }
  .tally.in-house { background: var(--green); }
  .tally.vesper { background: var(--teal); }
  .tally-row { display: flex; width: 110px; height: 31px; border: 1.5px solid var(--white); }
  .tally-row + .tally-row { margin-top: 14px; }
  .tally-label { width: 71px; display: flex; align-items: center; justify-content: center; font-weight: 700; font-size: 9.5px; letter-spacing: 0.3px; }
  .take-up .tally-label { background: var(--ink); color: var(--white); }
  .spend .tally-label { background: var(--orange); color: var(--ink); }
  .tally-value { flex: 1; display: flex; align-items: center; justify-content: center; font-family: "Oswald", sans-serif; font-size: 17px; }

  .footer-band {
    left: 0; top: 1017px; width: 702px; height: 75px; background: var(--plum-deep);
    text-align: center; font-weight: 500; font-size: 12.6px; line-height: 15.7px; padding-top: 13px;
  }
</style>
</head>
<body>
<main class="poster">
  <header class="abs headline-band">
    <div class="headline-main">MORE INCOME</div>
    <div class="headline-sub">BY LOOKING OUTSIDE YOUR 4 WALLS</div>
  </header>

  <div class="abs taglines">
    <p>PEOPLE WHO HOLD VESPERS ARE RECESSION PROOF</p>
    <p>IMMEDIATLEY IMPROVE YOUR CASH FLOW</p>
    <p>VESPER IS THE ANSWER</p>
  </div>

  <div class="abs brand"><span class="brand-dot"></span><span class="brand-name">Vesper</span></div>

  <h1 class="abs feature-title">Typical Ordering</h1>

  <div class="abs uplift"><div class="uplift-frame">326<sup>%</sup></div></div>

  <div class="abs covers-band">FOR 8 COVERS</div>

  <div class="abs divider-h"></div>
  <div class="abs divider-v"></div>

  <div class="abs column-head" style="left:37px">IN HOUSE <span>SPEND 532</span></div>
  <div class="abs column-head" style="left:369px">VESPER <span>SPEND 532</span></div>

  <!-- Left column -->
  <section class="abs course" style="left:37px; top:328px">
    <div class="course-head"><span class="course-name">Canapes</span><span class="price-tag">SELL PRICE | 8</span></div>
    <div class="mode-labels"><span>IN HOUSE ORDERING</span><span>VESPER ORDERING</span></div>
    <div class="course-boxes tight">
      <div class="tally in-house"><div class="tally-row take-up"><span class="tally-label">TAKE UP</span><span class="tally-value">0</span></div><div class="tally-row spend"><span class="tally-label">SPEND</span><span class="tally-value">0</span></div></div>
      <div class="tally vesper"><div class="tally-row take-up"><span class="tally-label">TAKE UP</span><span class="tally-value">16</span></div><div class="tally-row spend"><span class="tally-label">SPEND</span><span class="tally-value">128</span></div></div>
    </div>
  </section>

  <section class="abs course" style="left:37px; top:513px">
    <div class="course-head"><span class="course-name">Mains</span><span class="price-tag">SELL PRICE | 45</span></div>
    <div class="course-boxes">
      <div class="tally in-house"><div class="tally-row take-up"><span class="tally-label">TAKE UP</span><span class="tally-value">6</span></div><div class="tally-row spend"><span class="tally-label">SPEND</span><span class="tally-value">270</span></div></div>
      <div class="tally vesper"><div class="tally-row take-up"><span class="tally-label">TAKE UP</span><span class="tally-value">8</span></div><div class="tally-row spend"><span class="tally-label">SPEND</span><span class="tally-value">360</span></div></div>
    </div>
  </section>

  <section class="abs course" style="left:37px; top:679px">
    <div class="course-head"><span class="course-name">Desserts</span><span class="price-tag">SELL PRICE | 25</span></div>
    <div class="course-boxes">
      <div class="tally in-house"><div class="tally-row take-up"><span class="tally-label">TAKE UP</span><span class="tally-value">2</span></div><div class="tally-row spend"><span class="tally-label">SPEND</span><span class="tally-value">50</span></div></div>
      <div class="tally vesper"><div class="tally-row take-up"><span class="tally-label">TAKE UP</span><span class="tally-value">8</span></div><div class="tally-row spend"><span class="tally-label">SPEND</span><span class="tally-value">200</span></div></div>
    </div>
  </section>

  <section class="abs course" style="left:37px; top:844px">
    <div class="course-head"><span class="course-name">Cocktails</span><span class="price-tag">SELL PRICE | 25</span></div>
    <div class="course-boxes">
      <div class="tally in-house"><div class="tally-row take-up"><span class="tally-label">TAKE UP</span><span class="tally-value">2</span></div><div class="tally-row spend"><span class="tally-label">SPEND</span><span class="tally-value">50</span></div></div>
      <div class="tally vesper"><div class="tally-row take-up"><span class="tally-label">TAKE UP</span><span class="tally-value">8</span></div><div class="tally-row spend"><span class="tally-label">SPEND</span><span class="tally-value">200</span></div></div>
    </div>
  </section>

  <!-- Right column -->
  <section class="abs course" style="left:369px; top:328px">
    <div class="course-head"><span class="course-name">Entrée</span><span class="price-tag">SELL PRICE | 25</span></div>
    <div class="mode-labels"><span>IN HOUSE ORDERING</span><span>VESPER ORDERING</span></div>
    <div class="course-boxes tight">
      <div class="tally in-house"><div class="tally-row take-up"><span class="tally-label">TAKE UP</span><span class="tally-value">4</span></div><div class="tally-row spend"><span class="tally-label">SPEND</span><span class="tally-value">100</span></div></div>
      <div class="tally vesper"><div class="tally-row take-up"><span class="tally-label">TAKE UP</span><span class="tally-value">8</span></div><div class="tally-row spend"><span class="tally-label">SPEND</span><span class="tally-value">200</span></div></div>
    </div>
  </section>

  <section class="abs course" style="left:369px; top:513px">
    <div class="course-head"><span class="course-name">Entrée as Main</span><span class="price-tag">SELL PRICE | 25</span></div>
    <div class="course-boxes">
      <div class="tally in-house"><div class="tally-row take-up"><span class="tally-label">TAKE UP</span><span class="tally-value">2</span></div><div class="tally-row spend"><span class="tally-label">SPEND</span><span class="tally-value">50</span></div></div>
      <div class="tally vesper"><div class="tally-row take-up"><span class="tally-label">TAKE UP</span><span class="tally-value">0</span></div><div class="tally-row spend"><span class="tally-label">SPEND</span><span class="tally-value">0</span></div></div>
    </div>
  </section>

  <section class="abs course" style="left:369px; top:679px">
    <div class="course-head"><span class="course-name">Sides</span><span class="price-tag">SELL PRICE | 12</span></div>
    <div class="course-boxes">
      <div class="tally in-house"><div class="tally-row take-up"><span class="tally-label">TAKE UP</span><span class="tally-value">1</span></div><div class="tally-row spend"><span class="tally-label">SPEND</span><span class="tally-value">12</span></div></div>
      <div class="tally vesper"><div class="tally-row take-up"><span class="tally-label">TAKE UP</span><span class="tally-value">4</span></div><div class="tally-row spend"><span class="tally-label">SPEND</span><span class="tally-value">48</span></div></div>
    </div>
  </section>

  <section class="abs course" style="left:369px; top:844px">
    <div class="course-head"><span class="course-name">Staff</span><span class="price-tag">SELL PRICE | 300</span></div>
    <div class="course-boxes">
      <div class="tally in-house"><div class="tally-row take-up"><span class="tally-label">TAKE UP</span><span class="tally-value">0</span></div><div class="tally-row spend"><span class="tally-label">SPEND</span><span class="tally-value">0</span></div></div>
      <div class="tally vesper"><div class="tally-row take-up"><span class="tally-label">TAKE UP</span><span class="tally-value">2</span></div><div class="tally-row spend"><span class="tally-label">SPEND</span><span class="tally-value">600</span></div></div>
    </div>
  </section>

  <footer class="abs footer-band">
    <p>Achieve 3+ times the spend for the same number</p>
    <p>Cover your staff cost over and above your menu spend</p>
    <p>Vespers are an occasion and everyone has everything, cocktails, sides and canapes</p>
  </footer>
</main>
</body>
</html>
```